Firm of surveyors needs a professional yet friendly looking flyer

Our company offers help to landlords who have a phone mast on their property. We help them to negotiate the best rent and lease terms. There are so many landlords who don't seek professional advice because they don't know it's available. We want to send them a flyer which is informative, looks professional but also friendly so it prompts them to call us. I have attached the wording and some pictures but have more I can send but they were too large to attach.

Target Market(s)

Ranges from farmers to large corporations and land owners

Industry/Entity Type

Surveyor

Font styles to use
Sans Serif

Colors
acd136
9bcb3c
000000
ffffff
606060
848484

Requirements
Must have
• Must be clear, must give a professional look, must include pictures, must include our logo, must use our colour scheme (or variations of it). Ideally, I would like a try-fold design if possible.
Nice to have
• I would like there to be stand out lines to catch the readers eye (I have included some on the wording document). I would like a clean and modern design
Should not have
• Should not be too fussy

```html
<!DOCTYPE html>
<html lang="en">
<head>
<meta charset="utf-8">
<title>Ridgeway Mast Surveyors – Tri-fold Leaflet</title>
<link rel="stylesheet" href="https://fonts.googleapis.com/css2?family=Open+Sans:wght@400;600;700;800&family=Questrial&display=swap">
<style>
:root{
  --lime:#acd136;
  --green:#9bcb3c;
  --black:#000000;
  --white:#ffffff;
  --grey-dark:#606060;
  --grey:#848484;
  --charcoal:#2b2b2b;
  --backdrop:#e6e6e6;
  --sky-top:#1b4fa8;
  --sky-bottom:#cfdcf0;
}
*{box-sizing:border-box;margin:0;padding:0}
html,body{width:1200px;height:900px;overflow:hidden}
body{background:var(--backdrop);font-family:"Open Sans",Arial,sans-serif;color:var(--grey-dark);position:relative}
.spread{position:absolute;top:242px;width:588px;height:416px;display:flex;box-shadow:0 6px 22px rgba(0,0,0,.18)}
.spread--outside{left:8px}
.spread--inside{left:604px}
.panel{position:relative;width:196px;height:416px;overflow:hidden;background:var(--white)}
.panel svg.bg{position:absolute;inset:0;width:100%;height:100%}
.body-text{font-size:6.3px;line-height:1.5;text-align:justify}
.body-text p+p{margin-top:5px}
.photo{position:absolute;left:0;width:100%}

/* About panel */
.about{position:absolute;left:16px;right:16px;top:44px}
.about__title{font-family:"Questrial",sans-serif;color:var(--green);font-size:11px;font-weight:700;border-bottom:1px solid var(--green);padding-bottom:2px;margin-bottom:7px;display:inline-block}

/* Services panel */
.services{position:absolute;left:14px;right:10px;top:128px;color:var(--white)}
.services__title{font-family:"Questrial",sans-serif;font-size:15px;text-align:center;margin-bottom:8px}
.services__cols{display:flex;gap:8px;font-size:6.2px;line-height:1.45}
.services__cols ul{list-style:none;flex:1}
.services__cols li{position:relative;padding-left:7px;margin-bottom:2px}
.services__cols li::before{content:"";position:absolute;left:0;top:2.5px;width:3.5px;height:3.5px;background:var(--white)}
.contact{position:absolute;left:14px;right:10px;bottom:22px;color:var(--white);text-align:center;font-size:6.5px;line-height:1.55}
.contact__company{font-family:"Questrial",sans-serif;font-size:10.5px;margin-bottom:4px}
.contact__office{font-weight:700;text-decoration:underline;font-size:7.5px;margin-bottom:3px}

/* Cover */
.cover__photo{top:0;height:300px;background:linear-gradient(180deg,#2f6fc4 0%,#8fb3dd 45%,#c9d8e6 62%,#5e7b3a 70%,#3f5a25 100%)}
.headline{position:absolute;left:0;right:0;top:196px;text-align:center;color:var(--white);font-family:"Questrial",sans-serif;line-height:1.05}
.headline__lead{font-size:15px}
.headline__key{font-size:25px;color:var(--lime);font-weight:700}
.headline__band{display:inline-block;background:var(--green);color:var(--charcoal);font-size:11px;padding:1px 10px;margin:2px 0}
.headline__tail{font-size:13px}
.brand{position:absolute;left:0;right:0;top:334px;display:flex;align-items:center;justify-content:center;gap:8px}
.brand__dot{width:12px;height:12px;border-radius:50%;background:var(--green)}
.brand__name{font-family:"Questrial",sans-serif;font-size:15px;color:var(--grey-dark);line-height:1.15}

/* Inside */
.intro{position:absolute;left:14px;right:14px;top:14px}
.inside-left__photo{top:150px;height:222px;background:linear-gradient(180deg,var(--sky-top) 0%,#4f86d0 55%,var(--sky-bottom) 100%)}
.articles{position:absolute;left:14px;right:12px;top:42px;color:var(--white)}
.articles h2{font-family:"Open Sans",sans-serif;font-weight:800;font-size:8.5px;margin:6px 0 3px}
.articles h2:first-child{margin-top:0}
.articles .body-text{font-size:6px}
.advice{position:absolute;left:14px;right:14px;top:62px}
.advice__callout{font-weight:700;color:var(--charcoal);text-align:center;font-size:7px;line-height:1.35;margin:5px 0;border-bottom:1px solid var(--grey);padding-bottom:4px}
.inside-right__photo{top:256px;height:160px;background:linear-gradient(180deg,var(--sky-top) 0%,#5a8fd3 60%,#b8cde9 100%)}
</style>
</head>
<body>

<!-- Outside of the leaflet -->
<section class="spread spread--outside" aria-label="Leaflet outside">
  <article class="panel panel--about">
    <svg class="bg" viewBox="0 0 196 416" preserveAspectRatio="none" aria-hidden="true">
      <polygon points="0,0 196,0 196,30 0,12" fill="var(--charcoal)"/>
      <polygon points="120,0 196,0 196,14" fill="var(--green)"/>
      <polygon points="0,390 196,404 196,416 0,416" fill="var(--charcoal)"/>
    </svg>
    <div class="about">
      <h2 class="about__title">Ridgeway Mast Surveyors</h2>
      <div class="body-text">
        <p>Ridgeway Mast Surveyors is a firm of telecoms surveyors with over 15 years of experience dealing with mobile phone mast operators. We have built up a large database of thousands of comparable mobile phone mast deals to aid us in our telecoms negotiations. All of our surveyors have spent time working for phone mast operators and know the industry inside out. We now work exclusively for landlords, fighting your corner, ensuring our landlords get the highest rents and best lease terms available in the market place.</p>
        <p>Many of the original mobile phone mast leases and agreements are now coming up for renewal. This is an ideal opportunity for landlords to achieve the best deal. We are currently offering to review telecoms leases for free and provide landlords with our recommendations. If you would like to take us up on this free no obligation offer, send a copy of your agreement and any recent correspondence to us, either via post or email using the details on this flyer. Please also provide us with your name, contact number and let us know the current rent you are achieving, so we can see if there is room for improvement. Once we have received this, one of our surveyors will give you a call when convenient to talk through your lease with you, highlighting anything we feel needs addressing, any opportunity to increase the rent, or to discuss a specific issue you are having with your mast (i.e. an upgrade request).</p>
      </div>
    </div>
  </article>

  <article class="panel panel--services">
    <svg class="bg" viewBox="0 0 196 416" preserveAspectRatio="none" aria-hidden="true">
      <defs>
        <linearGradient id="greenFill" x1="0" y1="0" x2="0" y2="1">
          <stop offset="0" stop-color="var(--green)"/>
          <stop offset="1" stop-color="var(--lime)"/>
        </linearGradient>
      </defs>
      <rect width="196" height="416" fill="url(#greenFill)"/>
      <polygon points="0,0 196,0 196,60 0,118" fill="var(--charcoal)"/>
      <polygon points="0,118 196,60 196,66 0,126" fill="var(--white)" opacity=".85"/>
      <polygon points="0,390 196,416 0,416" fill="var(--charcoal)"/>
    </svg>
    <div class="services">
      <h2 class="services__title">Our Services</h2>
      <div class="services__cols">
        <ul>
          <li>Rent Reviews</li>
          <li>Lease Renewals</li>
          <li>Rent Protection</li>
          <li>Site Shares</li>
          <li>Safety Testing</li>
          <li>Equipment Upgrades</li>
        </ul>
        <ul>
          <li>Land Marketing for Masts</li>
          <li>Mast Sales and Marketing</li>
          <li>Network Consolidation Issues</li>
          <li>Mast Management and Portfolios</li>
          <li>Mast Removals / Decommissioning</li>
        </ul>
      </div>
    </div>
    <address class="contact" style="font-style:normal">
      <p class="contact__company">Ridgeway Mast Surveyors Ltd</p>
      <p class="contact__office">The Mill Offices,</p>
      <p>Beacon Business Park,</p>
      <p>Hollins Lane, Westshire, WS4 2QT</p>
      <p>T: 01632 960418 &nbsp;|&nbsp; F: 01632 960427</p>
      <p>E: hello@ridgewaymast.co.uk</p>
      <p>W: www.ridgewaymast.co.uk</p>
    </address>
  </article>

  <article class="panel panel--cover">
    <div class="photo cover__photo" role="img" aria-label="Photograph of a lattice phone mast standing in a green field under a blue sky"></div>
    <div class="headline">
      <div class="headline__lead">We Act</div>
      <div class="headline__key">Exclusively</div>
      <div class="headline__band">For Landlords On</div>
      <div class="headline__tail">All Phone Mast Matters</div>
    </div>
    <div class="brand">
      <span class="brand__dot" aria-hidden="true"></span>
      <span class="brand__name">Ridgeway Mast<br>Surveyors</span>
    </div>
  </article>
</section>

<!-- Inside of the leaflet -->
<section class="spread spread--inside" aria-label="Leaflet inside">
  <article class="panel panel--intro">
    <svg class="bg" viewBox="0 0 196 416" preserveAspectRatio="none" aria-hidden="true">
      <polygon points="0,372 196,360 196,416 0,416" fill="var(--charcoal)"/>
    </svg>
    <div class="intro body-text">
      <p>Recently, operators have been attempting to cut costs by reducing rents, ending leases or sharing sites with other networks. Many landlords are unaware of their rights and accept whatever is offered. Our surveyors can step in, review the terms proposed, and make sure any change is fair and the rent you receive reflects the true market value of your site. We protect your interests from the first letter to the final signature.</p>
    </div>
    <div class="photo inside-left__photo" role="img" aria-label="Photograph of a rooftop phone mast with antennas against a deep blue sky"></div>
  </article>

  <article class="panel panel--articles" style="background:var(--charcoal)">
    <svg class="bg" viewBox="0 0 196 416" preserveAspectRatio="none" aria-hidden="true">
      <polygon points="0,0 196,0 196,8 0,30" fill="var(--white)"/>
      <polygon points="0,30 196,8 196,22 0,36" fill="var(--green)"/>
      <polygon points="0,392 196,380 196,416 0,416" fill="var(--green)"/>
    </svg>
    <div class="articles">
      <h2>Sell Your Phone Mast</h2>
      <p class="body-text">We can also assist landlords in selling their phone mast site. There are investors who will pay a lump sum today in exchange for the future rental income. We will value your site and find the right buyer.</p>
      <h2>Getting A Phone Mast</h2>
      <p class="body-text">If you don't currently have a mast on your land but are interested in receiving an income from one, we offer a site marketing service. We promote your land to operators searching for new locations in your area.</p>
      <h2>The Current Telecoms Climate</h2>
      <p class="body-text">The telecoms market, in relation to mobile phone masts, is going through some huge changes. Operators are joining forces to share networks and cut costs, and many sites are being reviewed. What this means for landlords can be very confusing, and some changes may reduce your income. We know the industry and understand how a new deal could affect you, allowing us to provide the best advice on protecting your asset.</p>
    </div>
  </article>

  <article class="panel panel--advice">
    <svg class="bg" viewBox="0 0 196 416" preserveAspectRatio="none" aria-hidden="true">
      <polygon points="0,0 196,0 196,22 0,48" fill="var(--green)"/>
      <polygon points="120,0 196,0 196,14" fill="var(--charcoal)"/>
    </svg>
    <div class="advice">
      <p class="body-text">In April 2017 the Government introduced the Digital Economy Act. This sets out significant changes for landlords, including how rents are calculated. We have already seen operators contact landlords trying to reduce their rent in light of this new law. We are working alongside specialist telecoms solicitors to try to reduce the potential negative impact on landlords.</p>
      <p class="advice__callout">Landlords Should Not Sign Anything Until They Have Sought Professional Advice</p>
      <p class="body-text">Unsure Whether You Are Getting The Best Rent? Call Us Now For A Free, No Obligation Chat.</p>
      <p class="body-text" style="margin-top:4px">Our Expert Surveyors Will Be Happy To Help You Understand Proposed Changes And What They Could Mean For You.</p>
      <p class="body-text" style="margin-top:4px">Interested In Selling Your Site? Or Already Have An Offer? We Can Help You To Achieve The Best Sale Price, Quickly.</p>
    </div>
    <div class="photo inside-right__photo" role="img" aria-label="Photograph of a slim phone mast with antennas under a blue sky"></div>
    <svg class="bg" viewBox="0 0 196 416" preserveAspectRatio="none" aria-hidden="true" style="pointer-events:none">
      <polygon points="0,256 80,256 0,290" fill="var(--white)"/>
      <polygon points="196,380 196,416 120,416" fill="var(--green)"/>
    </svg>
  </article>
</section>

</body>
</html>
```